We are seeking two label designs for our premium pecan snack brand, MORVELO. MORVELO is known for its innovative pecan snacks, specifically a healthy and exotic blend of pecans, expertly salted, and infused with unique chili flavors. Our snacks are packaged in stand-up pouch bags, and we are looking for label designs product sizes - 5 oz. ( Size: 14 x 20 cm / 5.5 x 7.8 inches / Max Capacity: 16.2 oz)

Background Information:
MORVELO is a brand committed to offering a delightful snacking experience that combines the natural richness of pecans with the bold and exotic kick of carefully selected chilies. Our snacks cater to health-conscious consumers who appreciate the fusion of premium quality, unique flavors, and nutritional goodness.

Target Market(s)

Event Attendees (Entertainment Industry), Health-Conscious Consumers

Industry/Entity Type

Entertainment (sports events, arenas, stadiums, etc)

Font styles to use
Other font styles liked:
• Brother1816 Printed

Colors

Designer to choose colors to be used in the design.

Requirements
Must have
• Nutrition Fact (attached) , TRANSPARENT PART LIKE A WINDOW TO DISPLAY THE PRODUCT

```html
<!DOCTYPE html>
<html lang="en">
<head>
<meta charset="utf-8">
<title>MORVELO – Spicy Roasted Pecans Label</title>
<link href="https://fonts.googleapis.com/css2?family=Cabin:wght@500;600&family=Josefin+Sans:wght@300;600&family=Lato:wght@300;700&display=swap" rel="stylesheet">
<style>
  :root {
    --page: #ffffff;
    --ink-black: #1b1b1c;
    --charcoal: #2c2c2d;
    --cream: #ececea;
    --badge-grey: #dcdcdc;
    --chili: #d4572a;
    --chili-deep: #bf4a22;
    --badge-art: #e3a07c;
    --pecan: #8e4a28;
    --pecan-dark: #6a3219;
    --shell: #c08a62;
    --shell-dark: #93603e;
    --wood: #7a4a2a;
    --wood-dark: #5a3520;
    --window-light: #b87a52;
    --window-dark: #7e4328;
    --band-text: #f6e9e2;
    --dark-text: #2b2624;
  }
  * { margin: 0; padding: 0; box-sizing: border-box; }
  html, body { width: 1200px; height: 1200px; overflow: hidden; background: var(--page); }
  .canvas { position: relative; width: 1200px; height: 1200px; background: var(--page); }

  .label {
    position: absolute; left: 320px; top: 158px; width: 560px; height: 884px;
    overflow: hidden;
  }
  .label__top {
    position: absolute; left: 0; top: 0; width: 560px; height: 574px;
    background: radial-gradient(ellipse at 50% 60%, var(--charcoal) 0%, var(--ink-black) 72%);
  }

  .badge { position: absolute; left: 194px; top: 0; width: 172px; height: 178px; }
  .badge__shape { position: absolute; left: 0; top: 0; width: 172px; height: 178px; }
  .badge__art {
    position: absolute; left: 46px; top: 32px; width: 80px; height: 46px;
    border-radius: 50%; background: var(--badge-art);
  }
  .badge__premium, .badge__quality {
    position: absolute; left: 0; width: 172px; text-align: center;
    font-family: "Cabin", sans-serif; font-weight: 600; letter-spacing: 1px; line-height: 1;
  }
  .badge__premium { top: 103px; font-size: 17px; color: var(--chili); }
  .badge__quality { top: 125px; font-size: 19px; color: var(--ink-black); }

  .wordmark {
    position: absolute; left: 0; top: 204px; width: 560px; text-align: center;
    font-family: "Josefin Sans", sans-serif; font-weight: 600;
    font-size: 78px; letter-spacing: 2px; color: var(--cream); line-height: 1;
  }

  .photo-pecans {
    position: absolute; left: 8px; top: 338px; width: 150px; height: 200px;
    border-radius: 40px 70px 60px 30px;
    background: linear-gradient(160deg, var(--shell) 0%, var(--shell-dark) 100%);
  }
  .photo-bowl {
    position: absolute; left: 316px; top: 310px; width: 244px; height: 244px; border-radius: 50%;
    background: var(--wood);
    border: 10px solid var(--wood-dark);
  }
  .photo-bowl__fill {
    position: absolute; left: 22px; top: 22px; width: 180px; height: 180px; border-radius: 50%;
    background: linear-gradient(150deg, var(--pecan) 0%, var(--pecan-dark) 100%);
  }

  .claim {
    position: absolute; font-family: "Cabin", sans-serif; font-weight: 500;
    font-size: 27px; line-height: 33px; color: var(--cream);
  }
  .claim--salted { left: 198px; top: 340px; }
  .claim--chili { left: 198px; top: 462px; }
  .arrows { position: absolute; left: 0; top: 0; width: 560px; height: 574px; }

  .window {
    position: absolute; left: 0; top: 574px; width: 560px; height: 165px;
    background: linear-gradient(180deg, var(--window-dark) 0%, var(--window-light) 45%, var(--window-dark) 100%);
  }

  .label__band {
    position: absolute; left: 0; top: 739px; width: 560px; height: 145px;
    background: linear-gradient(180deg, var(--chili-deep) 0%, var(--chili) 100%);
    text-align: center;
  }
  .product-name {
    margin-top: 31px; font-family: "Josefin Sans", sans-serif; font-weight: 300;
    font-size: 23px; letter-spacing: 1.5px; color: var(--band-text); line-height: 1;
  }
  .net-weight {
    margin-top: 21px; font-family: "Lato", sans-serif; font-size: 18px; color: var(--dark-text); line-height: 1;
  }
  .net-weight strong { font-weight: 700; }
  .net-weight span { font-weight: 300; }
</style>
</head>
<body>
<main class="canvas">
  <section class="label" aria-label="MORVELO spicy roasted pecans pouch label">
    <div class="label__top">
      <div class="badge">
        <svg class="badge__shape" viewBox="0 0 172 178" aria-hidden="true">
          <path d="M0 0 V112 A86 66 0 0 0 172 112 V0 Z" fill="var(--ink-black)"/>
          <path d="M4 0 V110 A82 62 0 0 0 168 110 V0 Z" fill="var(--badge-grey)"/>
          <path d="M14 0 V108 A72 54 0 0 0 158 108 V0" fill="none" stroke="var(--ink-black)" stroke-width="2.5"/>
        </svg>
        <div class="badge__art" role="img" aria-label="Line drawing of pecans in shell and halves"></div>
        <div class="badge__premium">PREMIUM</div>
        <div class="badge__quality">QUALITY</div>
      </div>

      <div class="wordmark">MORVELO</div>

      <div class="photo-pecans" role="img" aria-label="Photo of whole pecans in shell and pecan halves"></div>
      <div class="photo-bowl" role="img" aria-label="Photo of a wooden bowl filled with roasted pecan halves">
        <div class="photo-bowl__fill"></div>
      </div>

      <p class="claim claim--salted">expertly<br>salted</p>
      <p class="claim claim--chili">chili<br>flavors</p>

      <svg class="arrows" viewBox="0 0 560 574" aria-hidden="true" fill="none" stroke="var(--cream)" stroke-width="2.5" stroke-linecap="round" stroke-linejoin="round">
        <path d="M130 450 C116 418 120 385 142 376 C160 370 162 396 148 398 C132 400 142 368 170 364 C178 363 184 366 190 372"/>
        <path d="M180 364 L191 373 L178 380"/>
        <path d="M358 486 C358 526 330 548 298 536 C290 533 284 528 280 522"/>
        <path d="M278 534 L279 521 L292 524"/>
      </svg>
    </div>

    <div class="window" role="img" aria-label="Clear window showing the roasted pecan halves inside"></div>

    <div class="label__band">
      <p class="product-name">SPICY ROASTED PECANS</p>
      <p class="net-weight"><strong>net wt: 5 oz.</strong> <span>(142 gr.)</span></p>
    </div>
  </section>
</main>
</body>
</html>
```